Bref créative
VPrestige
Vantorel Prestige
Professional
Marc Lindqvora
President
47219 Brookfern Hollow Lane
Roswell, Georgia 30982
mlind@vantorelprestige.example
www.vantorelprestige.example
Need business card and stationary design. Have uploaded new logo.

```html
<!DOCTYPE html>
<html lang="en">
<head>
<meta charset="utf-8">
<title>Vantorel Prestige — Stationery</title>
<link rel="stylesheet" href="https://fonts.googleapis.com/css2?family=PT+Sans:wght@400;700&display=swap">
<style>
  :root {
    --navy: #2c2a6b;
    --gold: #d9a23a;
    --paper: #ffffff;
    --stage: #ffffff;
    --edge: #d8d8dc;
    --ink: #4a4a58;
    --shadow: rgba(0,0,0,0.18);
  }
  * { box-sizing: border-box; margin: 0; padding: 0; }
  html, body { width: 1200px; height: 681px; overflow: hidden; background: var(--stage); }
  body { font-family: "PT Sans", sans-serif; color: var(--ink); }
  .canvas { position: relative; width: 1200px; height: 681px; }

  .sheet {
    position: absolute;
    background: var(--paper);
    border: 1px solid var(--edge);
    box-shadow: 2px 3px 6px var(--shadow);
  }
  .envelope-front { left: 60px; top: 98px; width: 487px; height: 211px; }
  .envelope-back  { left: 60px; top: 360px; width: 487px; height: 228px; }
  .letterhead     { left: 619px; top: 48px; width: 377px; height: 581px; }
  .business-card  { left: 972px; top: 180px; width: 168px; height: 103px; }

  .brand-name {
    position: absolute;
    font-weight: 700;
    color: var(--navy);
    white-space: nowrap;
    line-height: 1;
  }
  .brand-dot {
    display: inline-block;
    border-radius: 50%;
    background: var(--gold);
    vertical-align: middle;
  }

  .top-rule {
    position: absolute;
    height: 3px;
    background: linear-gradient(90deg, rgba(217,162,58,0) 0%, var(--gold) 35%, var(--gold) 70%, var(--navy) 100%);
  }
  .bottom-band {
    position: absolute;
    left: 0;
    background: linear-gradient(90deg, var(--navy) 0%, var(--navy) 30%, var(--gold) 70%, rgba(217,162,58,0) 100%);
  }

  .address {
    position: absolute;
    right: 12px;
    text-align: right;
    color: var(--ink);
    line-height: 1.35;
    white-space: nowrap;
  }

  /* envelope front */
  .envelope-front .brand-name { left: 16px; top: 24px; font-size: 15px; }
  .envelope-front .brand-dot { width: 10px; height: 10px; margin-right: 5px; }
  .envelope-front .top-rule { left: 150px; right: 0; top: 48px; }
  .envelope-front .bottom-band { top: 185px; width: 240px; height: 5px; }
  .envelope-front .address { bottom: 12px; font-size: 7px; }

  /* envelope back */
  .envelope-back .flap { position: absolute; inset: 0; width: 100%; height: 100%; }
  .envelope-back .brand-name { left: 50%; top: 22px; transform: translateX(-50%); font-size: 12px; }

  /* letterhead */
  .letterhead .brand-name { left: 16px; top: 34px; font-size: 15px; }
  .letterhead .brand-dot { width: 10px; height: 10px; margin-right: 5px; }
  .letterhead .top-rule { left: 170px; right: 0; top: 58px; }
  .letterhead .bottom-band { top: 551px; width: 210px; height: 6px; }
  .letterhead .address { bottom: 34px; font-size: 7px; }

  /* business card */
  .business-card .brand-name { left: 8px; top: 14px; font-size: 8px; }
  .business-card .brand-dot { width: 6px; height: 6px; margin-right: 3px; }
  .business-card .top-rule { left: 70px; right: 0; top: 26px; height: 2px; }
  .business-card .person { position: absolute; left: 60px; top: 36px; font-size: 5px; line-height: 1.35; color: var(--ink); }
  .business-card .person .name { font-weight: 700; color: var(--navy); }
  .business-card .address { right: 8px; top: 44px; font-size: 4.2px; }
  .business-card .bottom-band { top: 86px; width: 110px; height: 3px; }
</style>
</head>
<body>
<main class="canvas">

  <section class="sheet envelope-front" aria-label="Envelope front">
    <div class="brand-name"><span class="brand-dot"></span>Vantorel Prestige</div>
    <div class="top-rule"></div>
    <div class="bottom-band"></div>
    <p class="address">47219 Brookfern Hollow Lane, Harlow Glen, Vermont 30982</p>
  </section>

  <section class="sheet envelope-back" aria-label="Envelope back">
    <svg class="flap" viewBox="0 0 487 228" preserveAspectRatio="none" aria-hidden="true">
      <path d="M4 4 C 10 20, 20 40, 60 70 Q 200 108 243 110 Q 286 108 427 70 C 467 40, 477 20, 483 4"
            fill="none" stroke="#9a9aa3" stroke-width="1"/>
    </svg>
    <div class="brand-name">Vantorel Prestige</div>
  </section>

  <section class="sheet letterhead" aria-label="Letterhead">
    <div class="brand-name"><span class="brand-dot"></span>Vantorel Prestige</div>
    <div class="top-rule"></div>
    <div class="bottom-band"></div>
    <p class="address">47219 Brookfern Hollow Lane, Harlow Glen, Vermont 30982<br>P: 802.555.0142 | www.vantorelprestige.example</p>
  </section>

  <section class="sheet business-card" aria-label="Business card">
    <div class="brand-name"><span class="brand-dot"></span>Vantorel Prestige</div>
    <div class="top-rule"></div>
    <p class="person"><span class="name">Marc Lindqvora</span><br>President</p>
    <p class="address">47219 Brookfern Hollow Lane<br>Harlow Glen, Vermont 30982<br>P: 802.555.0142<br>F: 802.555.0143<br>mlind@vantorelprestige.example<br>www.vantorelprestige.example</p>
    <div class="bottom-band"></div>
  </section>

</main>
</body>
</html>
```